Online business manager needs a website

I need a website designed and then coded. I am an online business manager serving a number of different industries providing administrative support to existing small businesses and helping solo practitioners get their new business up and running.

I didn't have a logo formally designed but have been using the attached avatar and wouldn't mind something that incorporated that.

The business doesn't have an official name, so I've just been using my name Lena Pruvost, Online Business Manager or Lena Pruvost, OBM. I've attached two documents that I have made previously for an example of content.

I would prefer the final site be in Wordpress.

Requirements
Must have
• A way to contact me, testimonials, list of services

```html
<!DOCTYPE html>
<html lang="en">
<head>
<meta charset="utf-8">
<title>Lena Pruvost — Online Business Manager</title>
<link href="https://fonts.googleapis.com/css2?family=Poppins:wght@400;500;600;700&display=swap" rel="stylesheet">
<style>
:root{
  --green:#1a6b4a;
  --green-dark:#134a34;
  --ink:#222;
  --text:#555;
  --muted:#777;
  --light:#f1f1f1;
  --line:#dcdcdc;
  --footer:#2a2a2a;
  --white:#fff;
}
*{margin:0;padding:0;box-sizing:border-box}
html,body{width:1200px;height:4286px;overflow:hidden}
body{position:relative;font-family:"Poppins",sans-serif;color:var(--ink);background:var(--white)}
.abs{position:absolute}
.ph{position:absolute}
.label{position:absolute;font-size:14px;font-weight:600;color:var(--green);letter-spacing:.5px;text-transform:uppercase}
.title{position:absolute;font-size:32px;font-weight:600;color:var(--ink)}
.center{left:0;width:1200px;text-align:center}
.btn{position:absolute;display:flex;align-items:center;justify-content:center;border-radius:22px;font-size:12px;font-weight:600}
.btn-solid{background:var(--green);color:var(--white)}
.btn-ghost{background:var(--white);color:var(--green);box-shadow:0 2px 8px rgba(0,0,0,.12)}
.vline{position:absolute;width:1px;background:var(--line)}
.hline{position:absolute;height:1px;background:var(--line)}

.hero-bg{left:0;top:0;width:644px;height:629px;background:var(--light)}
.hero-photo{left:644px;top:0;width:556px;height:629px;background:linear-gradient(135deg,#6f7a55,#c9b193 50%,#3f5a2e)}
.nav{left:644px;top:0;width:556px;height:97px;background:rgba(40,40,40,.85)}
.nav a{position:absolute;top:42px;font-size:11px;color:var(--white);text-decoration:none;letter-spacing:.3px}
.nav a.active{color:#3bbf86}
.avatar{left:112px;top:25px;width:129px;height:108px;background:linear-gradient(#e6d7a6,#5c6e7a);border-radius:6px}
.social{top:37px;width:26px;height:26px;border-radius:50%;background:#c9c9c9}
.hello{left:112px;top:233px;font-size:20px;font-weight:500}
.name{left:110px;top:262px;font-size:72px;font-weight:700;color:var(--green);letter-spacing:-1px}
.role{left:112px;top:362px;font-size:28px;font-weight:400;letter-spacing:.5px}

.arrow{width:28px;height:28px;border-radius:50%;background:#d2d2d2;display:flex;align-items:center;justify-content:center}
.brand{top:690px;font-size:30px;font-weight:600;color:#111;transform:translateX(-50%)}

.about-p1{left:112px;top:870px;width:316px;height:370px;background:linear-gradient(160deg,#b04a8a,#2b2b3a 60%,#1c1c24)}
.about-p2{left:296px;top:1048px;width:227px;height:238px;background:linear-gradient(160deg,#6a6f77,#d7b98b);border:6px solid var(--white)}
.about-text{left:609px;top:974px;width:410px;font-size:11px;line-height:18.7px;color:var(--text)}
.contact-line{font-size:12px;color:var(--ink);white-space:nowrap}
.contact-line b{font-weight:600}

.svc-icon{position:absolute;width:50px;height:46px}
.svc-title{position:absolute;font-size:17px;font-weight:500;line-height:22px;color:var(--ink)}
.svc-list{position:absolute;font-size:10px;line-height:15px;color:var(--muted)}

.edu-bg{left:0;top:1756px;width:1200px;height:544px;background:var(--light)}
.edu-photo{left:0;top:1756px;width:527px;height:544px;background:linear-gradient(150deg,#d6cbb8,#b89372 55%,#5f5547)}
.edu-name{position:absolute;left:609px;font-size:13px;font-weight:600}
.edu-sub{position:absolute;left:609px;font-size:10px;color:var(--text);letter-spacing:1px}

.gal-bg{left:0;top:2820px;width:1200px;height:500px;background:var(--light)}
.card{top:2990px;height:267px}

.testi-bg{left:0;top:3320px;width:1200px;height:400px;background:linear-gradient(90deg,#1c5e44,#143f2e)}
.testi-photo{left:0;top:3356px;width:428px;height:364px;background:linear-gradient(160deg,#8a9a5a,#6b4a3a 55%,#9a3a3a)}
.dot{top:3629px;width:8px;height:8px;border-radius:50%;background:rgba(255,255,255,.5)}

.price{position:absolute;width:240px;text-align:center;transform:translateX(-50%)}
.price .amt{font-size:30px;font-weight:600;color:var(--green)}
.price .hrs{font-size:11px;margin-top:4px}
.price .desc{font-size:10px;line-height:16px;color:var(--muted);margin-top:12px}

.footer{left:0;top:4077px;width:1200px;height:209px;background:var(--footer);color:var(--white)}
.f-head{position:absolute;font-size:12px;font-weight:600;text-transform:uppercase}
.f-link{position:absolute;font-size:10px;color:#ddd}
.f-dot{display:inline-block;width:14px;height:14px;border-radius:50%;background:#fff;vertical-align:middle;margin-right:8px}
</style>
</head>
<body>

<div class="abs hero-bg"></div>
<div class="ph hero-photo" role="img" aria-label="Photo of Lena working on a laptop beside green plants"></div>
<nav class="abs nav">
  <a class="active" style="left:72px">HOME</a>
  <a style="left:141px">ABOUT</a>
  <a style="left:206px">SKILL</a>
  <a style="left:280px">SERVICES</a>
  <a style="left:374px">TESTIMONIAL</a>
  <a style="left:472px">CONTACT</a>
</nav>
<div class="ph avatar" role="img" aria-label="Avatar logo: cartoon of Lena waving from a laptop screen"></div>
<div class="abs social" style="left:380px"></div>
<div class="abs social" style="left:418px"></div>
<div class="abs social" style="left:457px"></div>
<div class="abs social" style="left:496px"></div>
<div class="abs hello">HELLO, I AM</div>
<div class="abs name">Lena Pruvost</div>
<div class="abs role">Online Business Manager</div>
<div class="btn btn-solid" style="left:113px;top:424px;width:147px;height:42px">Get Started</div>
<div class="btn btn-ghost" style="left:280px;top:424px;width:145px;height:42px">Hire Me</div>

<div class="abs arrow" style="left:111px;top:697px"><svg width="10" height="10" viewBox="0 0 10 10"><path d="M6.5 1.5 3 5l3.5 3.5" stroke="#fff" stroke-width="1.6" fill="none"/></svg></div>
<div class="abs arrow" style="left:1060px;top:697px"><svg width="10" height="10" viewBox="0 0 10 10"><path d="M3.5 1.5 7 5 3.5 8.5" stroke="#fff" stroke-width="1.6" fill="none"/></svg></div>
<div class="abs brand" style="left:326px">Circlebook</div>
<div class="abs brand" style="left:514px">Snapgrid</div>
<div class="abs brand" style="left:702px">Deskware</div>
<div class="abs brand" style="left:880px">Artboard</div>
<div class="hline" style="left:138px;top:804px;width:924px"></div>

<div class="ph about-p1" role="img" aria-label="Portrait photo of Lena in front of flowering bushes"></div>
<div class="ph about-p2" role="img" aria-label="Portrait photo of Lena outdoors in a city street"></div>
<div class="label" style="left:609px;top:882px">About Me</div>
<div class="title" style="left:609px;top:905px">Myself Lena Pruvost</div>
<p class="abs about-text">Hi! I'm so excited that you have chosen to explore my portfolio. Helping businesses achieve their goals is my passion, and I'm thrilled that with my assistance you will have more time for your own passion project. I thrive while working independently, which means you can be confident when leaving tasks for me. The type of work that lights me up is anything involving organization and/or spreadsheets. You need data analyzed that includes multiple nested if formulas? You have an overwhelming amount of email to sort through and appointments to book? I'm your gal!</p>
<div class="abs contact-line" style="left:609px;top:1162px"><b>Circlebook :</b> /lenapruvost</div>
<div class="abs contact-line" style="left:803px;top:1162px"><b>Phone :</b> 555.014.2280</div>
<div class="abs contact-line" style="left:609px;top:1193px"><b>Email :</b> hello@lenapruvost-obm.com</div>
<div class="abs contact-line" style="left:860px;top:1193px"><b>Worknet :</b> Lena M. Pruvost</div>
<div class="btn btn-solid" style="left:609px;top:1239px;width:147px;height:39px">Contact Me</div>

<div class="label center" style="top:1358px">What I Offer</div>
<div class="title center" style="top:1382px">My Services</div>
<div class="vline" style="left:309px;top:1461px;height:219px"></div>
<div class="vline" style="left:579px;top:1461px;height:219px"></div>
<div class="vline" style="left:849px;top:1461px;height:219px"></div>

<svg class="svc-icon" style="left:110px;top:1476px" viewBox="0 0 50 46"><circle cx="34" cy="12" r="12" fill="#e7e7e7"/><rect x="3" y="12" width="34" height="24" rx="3" fill="none" stroke="#1a6b4a" stroke-width="2.5"/><circle cx="20" cy="22" r="5" fill="none" stroke="#1a6b4a" stroke-width="2"/><path d="M13 42h14M20 36v6" stroke="#1a6b4a" stroke-width="2.5"/></svg>
<div class="svc-title" style="left:112px;top:1545px">Virtual Assistance</div>
<div class="svc-list" style="left:112px;top:1578px">Calendar Management<br>Email Management Light<br>Graphic Design Data Entry</div>

<svg class="svc-icon" style="left:348px;top:1476px" viewBox="0 0 50 46"><circle cx="34" cy="12" r="12" fill="#e7e7e7"/><rect x="3" y="8" width="28" height="34" rx="2" fill="none" stroke="#1a6b4a" stroke-width="2.5"/><path d="M9 16h16M9 23h12M9 30h8M26 30l10 10" stroke="#1a6b4a" stroke-width="2.5"/></svg>
<div class="svc-title" style="left:350px;top:1545px">Social Media &amp;<br>Content Management</div>
<div class="svc-list" style="left:350px;top:1600px">Content Repurposing Graphics<br>Creation Audiogram Creation<br>Search Engine Optimization</div>

<svg class="svc-icon" style="left:619px;top:1476px" viewBox="0 0 50 46"><circle cx="34" cy="12" r="12" fill="#e7e7e7"/><rect x="3" y="8" width="26" height="34" rx="2" fill="none" stroke="#1a6b4a" stroke-width="2.5"/><path d="M8 16l2 2 4-4M8 26l2 2 4-4M17 16h8M17 26h8M28 42l10-14 4 4-10 14z" stroke="#1a6b4a" stroke-width="2" fill="none"/></svg>
<div class="svc-title" style="left:621px;top:1545px">Finance Management</div>
<div class="svc-list" style="left:621px;top:1578px">Create Invoices Track<br>Receivables Analyze Expenses<br>Year Over Year Analytics</div>

<svg class="svc-icon" style="left:888px;top:1476px" viewBox="0 0 50 46"><circle cx="30" cy="12" r="12" fill="#e7e7e7"/><rect x="3" y="16" width="44" height="26" rx="3" fill="none" stroke="#1a6b4a" stroke-width="2.5"/><path d="M18 16v-5h14v5M3 27h44M22 27v5h6v-5" stroke="#1a6b4a" stroke-width="2.5" fill="none"/></svg>
<div class="svc-title" style="left:890px;top:1545px">Business Management</div>
<div class="svc-list" style="left:890px;top:1578px">Creation of Operating Procedures<br>Review of Website Strategy<br>Reporting and Analytics<br>Project Management</div>

<div class="abs edu-bg"></div>
<div class="ph edu-photo" role="img" aria-label="Photo of a woman reading a book at a café table"></div>
<div class="label" style="left:609px;top:1817px">Knowlodege</div>
<div class="title" style="left:609px;top:1840px">My Education</div>
<div class="edu-name" style="top:1915px">Virtual Assistant Internship</div>
<div class="edu-sub" style="top:1937px">90 DAY VA CERTIFICATE</div>
<div class="hline" style="left:609px;top:1982px;width:406px"></div>
<div class="edu-name" style="top:2010px">Marisol Vega Virtual Services</div>
<div class="edu-sub" style="top:2032px">INTERNSHIP</div>
<div class="hline" style="left:609px;top:2077px;width:406px"></div>
<div class="edu-name" style="top:2106px">Northfield State College</div>
<div class="edu-sub" style="top:2128px">MBA - LEADERSHIP</div>
<div class="hline" style="left:609px;top:2173px;width:406px"></div>
<div class="edu-name" style="top:2202px">Eastbrook University</div>
<div class="edu-sub" style="top:2224px">BFA - THEATRE ARTS</div>

<div class="label center" style="top:2372px">Services</div>
<div class="title center" style="top:2396px">What I Do Best</div>
<div class="vline" style="left:331px;top:2476px;height:211px"></div>
<div class="vline" style="left:599px;top:2476px;height:211px"></div>
<div class="vline" style="left:867px;top:2476px;height:211px"></div>

<svg class="svc-icon" style="left:110px;top:2494px" viewBox="0 0 50 46"><circle cx="34" cy="12" r="12" fill="#e7e7e7"/><rect x="3" y="10" width="32" height="32" rx="2" fill="none" stroke="#1a6b4a" stroke-width="2.5"/><path d="M3 18h32M9 26h14M9 33h10M26 38l12-14" stroke="#1a6b4a" stroke-width="2.5"/></svg>
<div class="svc-title" style="left:112px;top:2558px">Content<br>Repurposing</div>
<div class="svc-list" style="left:112px;top:2605px">Lorem ipsum dolor sit amet,<br>consectetur adipiscing elit, sed<br>do eiusmod tempor incididunt ut<br>labore et dolore magna aliqua.</div>

<svg class="svc-icon" style="left:377px;top:2494px" viewBox="0 0 50 46"><circle cx="34" cy="12" r="12" fill="#e7e7e7"/><path d="M3 18h14l3 4h20v20H3z" fill="none" stroke="#1a6b4a" stroke-width="2.5"/><path d="M9 18v-6h10l3 4h16v6" fill="none" stroke="#1a6b4a" stroke-width="2"/></svg>
<div class="svc-title" style="left:379px;top:2558px">Data Entry</div>
<div class="svc-list" style="left:379px;top:2605px">Lorem ipsum dolor sit amet,<br>consectetur adipiscing elit, sed<br>do eiusmod tempor incididunt ut<br>labore et dolore magna aliqua.</div>

<svg class="svc-icon" style="left:645px;top:2494px" viewBox="0 0 50 46"><circle cx="25" cy="10" r="8" fill="none" stroke="#1a6b4a" stroke-width="2.5"/><path d="M3 20h44v22H3zM3 20l22 14 22-14M3 42l16-12M47 42 31 30" fill="none" stroke="#1a6b4a" stroke-width="2.5"/></svg>
<div class="svc-title" style="left:647px;top:2558px">Email<br>Management</div>
<div class="svc-list" style="left:647px;top:2605px">Lorem ipsum dolor sit amet,<br>consectetur adipiscing elit, sed<br>do eiusmod tempor incididunt ut<br>labore et dolore magna aliqua.</div>

<svg class="svc-icon" style="left:913px;top:2494px" viewBox="0 0 50 46"><circle cx="30" cy="12" r="12" fill="#e7e7e7"/><rect x="3" y="6" width="24" height="36" rx="2" fill="none" stroke="#1a6b4a" stroke-width="2.5"/><rect x="16" y="22" width="22" height="20" rx="2" fill="#fff" stroke="#1a6b4a" stroke-width="2.5"/><path d="M21 28h12M21 33h12M21 38h12" stroke="#1a6b4a" stroke-width="2"/></svg>
<div class="svc-title" style="left:915px;top:2558px">Bookkeeping</div>
<div class="svc-list" style="left:915px;top:2605px">Lorem ipsum dolor sit amet,<br>consectetur adipiscing elit, sed<br>do eiusmod tempor incididunt ut<br>labore et dolore magna aliqua.</div>

<div class="abs arrow" style="left:569px;top:2719px"><svg width="10" height="10" viewBox="0 0 10 10"><path d="M6.5 1.5 3 5l3.5 3.5" stroke="#fff" stroke-width="1.6" fill="none"/></svg></div>
<div class="abs arrow" style="left:603px;top:2719px"><svg width="10" height="10" viewBox="0 0 10 10"><path d="M3.5 1.5 7 5 3.5 8.5" stroke="#fff" stroke-width="1.6" fill="none"/></svg></div>

<div class="abs gal-bg"></div>
<div class="label" style="left:112px;top:2884px">Gallery</div>
<div class="title" style="left:112px;top:2908px">My Works</div>
<div class="abs arrow" style="left:1027px;top:2891px"><svg width="10" height="10" viewBox="0 0 10 10"><path d="M6.5 1.5 3 5l3.5 3.5" stroke="#fff" stroke-width="1.6" fill="none"/></svg></div>
<div class="abs arrow" style="left:1061px;top:2891px"><svg width="10" height="10" viewBox="0 0 10 10"><path d="M3.5 1.5 7 5 3.5 8.5" stroke="#fff" stroke-width="1.6" fill="none"/></svg></div>
<div class="ph card" style="left:112px;width:252px;background:#f0555a" role="img" aria-label="Social media graphic on coral background"></div>
<div class="ph card" style="left:391px;width:266px;background:linear-gradient(160deg,#fbeee6,#f3d9c9)" role="img" aria-label="Webinar promo graphic with two speaker photos"></div>
<div class="ph card" style="left:684px;width:266px;background:#fff;border:5px solid #2a2f6a" role="img" aria-label="Podcast episode promo graphic with guest photos"></div>
<div class="ph card" style="left:975px;width:225px;background:linear-gradient(160deg,#f3d3d6,#e9bfc4)" role="img" aria-label="Podcast episode cover with headphones"></div>

<div class="abs testi-bg"></div>
<div class="ph testi-photo" role="img" aria-label="Photo of a smiling client"></div>
<svg class="abs" style="left:526px;top:3474px" width="60" height="48" viewBox="0 0 60 48"><path d="M2 46V26C2 12 10 4 24 2v9c-7 2-10 6-10 13h10v22zM34 46V26c0-14 8-22 22-24v9c-7 2-10 6-10 13h10v22z" fill="#0d2a1f"/></svg>
<div class="label" style="left:609px;top:3400px;color:#fff">Testimonials</div>
<div class="title" style="left:609px;top:3424px;color:#fff">Client Love</div>
<div class="abs" style="left:609px;top:3487px;font-size:12px;font-weight:600;color:#fff">Dana R. Holloway, Owner, Brightpath Roofing</div>
<p class="abs" style="left:609px;top:3518px;width:440px;font-size:11px;line-height:16px;color:#fff">When it became apparent that a project would take more time than I had, Lena stepped up to take on the required research. She was thorough and timely; able to meet a last-minute 12-hour deadline. I would highly recommend Lena to assist with your next project.</p>
<div class="abs dot" style="left:996px;background:#fff"></div>
<div class="abs dot" style="left:1018px"></div>
<div class="abs dot" style="left:1040px"></div>

<div class="label center" style="top:3732px">Pricing</div>
<div class="title center" style="top:3756px">Rates And Packages</div>
<div class="vline" style="left:323px;top:3810px;height:200px"></div>
<div class="vline" style="left:599px;top:3810px;height:200px"></div>
<div class="vline" style="left:875px;top:3810px;height:200px"></div>
<div class="price" style="left:185px;top:3828px"><div class="amt">$40</div><div class="hrs">Hourly Rate</div><div class="desc">For clients needing<br>only occasional help</div></div>
<div class="price" style="left:461px;top:3828px"><div class="amt">$700</div><div class="hrs">20 hours/month</div><div class="desc">Includes one 15 minute<br>meeting per week</div></div>
<div class="price" style="left:737px;top:3828px"><div class="amt">$1,300</div><div class="hrs">40 hours/month</div><div class="desc">Includes one 30 minute<br>meeting per week</div></div>
<div class="price" style="left:1013px;top:3828px"><div class="amt">$2,400</div><div class="hrs">80 hours/month</div><div class="desc">Includes one 60 minute<br>meeting per week</div></div>
<div class="btn btn-ghost" style="left:112px;top:3960px;width:146px;height:40px">Enoroll Now</div>
<div class="btn btn-solid" style="left:388px;top:3960px;width:146px;height:40px">Enoroll Now</div>
<div class="btn btn-ghost" style="left:664px;top:3960px;width:146px;height:40px">Enoroll Now</div>
<div class="btn btn-ghost" style="left:940px;top:3960px;width:146px;height:40px">Enoroll Now</div>

<footer class="abs footer">
  <div class="ph" style="left:200px;top:40px;width:114px;height:88px;background:linear-gradient(#e6d7a6,#5c6e7a);border-radius:6px" role="img" aria-label="Avatar logo: cartoon of Lena waving from a laptop screen"></div>
  <div class="hline" style="left:112px;top:147px;width:276px;background:#666"></div>
  <div class="abs" style="left:145px;top:159px;font-size:10px;color:#ddd">Copyright © 2010–2023 All rights reserved.</div>

  <div class="f-head" style="left:458px;top:46px">Digital Business Manager</div>
  <p class="abs" style="left:458px;top:80px;width:235px;font-size:10px;line-height:13px;color:#ddd">Focused on the live event and entertainment industry. Helping artists and owners to better manage their career and business by strategically reviewing systems, recommending operational efficiencies, and managing inboxes.</p>

  <div class="f-head" style="left:782px;top:46px">About Me</div>
  <div class="f-link" style="left:782px;top:80px">My history</div>
  <div class="f-link" style="left:782px;top:102px">Experience</div>
  <div class="f-link" style="left:782px;top:124px">Services</div>
  <div class="f-link" style="left:782px;top:146px">Blog</div>

  <div class="f-head" style="left:957px;top:46px">Follow Me On</div>
  <div class="f-link" style="left:957px;top:76px"><span class="f-dot"></span>Circlebook</div>
  <div class="f-link" style="left:957px;top:98px"><span class="f-dot"></span>Pinboardly</div>
  <div class="f-link" style="left:957px;top:120px"><span class="f-dot"></span>Snapgrid</div>
  <div class="f-link" style="left:957px;top:142px"><span class="f-dot"></span>Chirpline</div>
</footer>

</body>
</html>
```